Power Point Template for Company

I would like a power point template for my company. This will be the template that we use for all presentations. I have attached our company logo and would like it incorporated into the template. Thanks.

```html
<!DOCTYPE html>
<html lang="en">
<head>
<meta charset="utf-8">
<title>Larkfield Studio – Presentation Template</title>
<link href="https://fonts.googleapis.com/css2?family=Montserrat:wght@400;500;600;700;800&display=swap" rel="stylesheet">
<style>
:root{
  --orange:#f47a1f;
  --ink:#1a1a1a;
  --text:#333333;
  --muted:#555555;
  --panel:#ffffff;
  --slide-grey:#eeeeee;
  --page:#d9d9d9;
  --rule:#dddddd;
}
*{margin:0;padding:0;box-sizing:border-box}
html,body{width:1200px;height:3810px;overflow:hidden}
body{background:var(--page);font-family:'Montserrat',sans-serif;color:var(--text);position:relative}
.slide{position:absolute;left:89px;width:1022px;height:575px;overflow:hidden;background:var(--panel)}
.slide.grey{background:var(--slide-grey)}
.abs{position:absolute}
.topline{position:absolute;left:0;top:0;width:100%;height:5px;background:var(--orange)}
.tab{position:absolute;left:0;top:0;height:34px;background:var(--orange);color:#fff;font-size:11px;font-weight:700;letter-spacing:.3px;padding:13px 0 0 38px;clip-path:polygon(0 0,100% 0,calc(100% - 22px) 100%,0 100%)}
.footer-brand{position:absolute;left:33px;top:521px;display:flex;align-items:center;gap:8px}
.footer-brand .dot{width:30px;height:30px;border-radius:50%;background:var(--orange)}
.footer-brand .name{font-size:13px;font-weight:800;color:var(--ink);letter-spacing:.5px}
.page-no{position:absolute;left:961px;top:520px;width:27px;height:27px;background:var(--orange);color:#fff;font-size:12px;display:flex;align-items:center;justify-content:center}
.slide-title{position:absolute;left:0;width:100%;text-align:center;font-size:31px;font-weight:800;color:var(--ink)}

/* cover */
.cover{background:#000}
.cover-photo{position:absolute;inset:0;background:radial-gradient(circle at 30% 40%,#2a2118 0%,#111 55%,#050505 100%)}
.cover-frame{position:absolute;left:56px;top:40px;width:909px;height:487px;border:4px solid #fff}
.cover-mark{position:absolute;left:411px;top:95px;width:200px;height:200px;border-radius:50%;background:var(--orange)}
.cover-name{position:absolute;left:0;width:100%;top:380px;text-align:center;color:#fff;font-size:72px;font-weight:800;letter-spacing:2px}

/* about */
.about-title{position:absolute;left:38px;top:86px;font-size:30px;font-weight:800;color:var(--ink)}
.about-text{position:absolute;left:38px;top:135px;width:466px;font-size:16px;line-height:24.6px;text-align:justify;color:var(--text)}
.about-photo{position:absolute;left:569px;top:84px;width:406px;height:406px;border-radius:50%;background:radial-gradient(circle at 40% 35%,#e08a3a 0%,#b85a1a 45%,#5a2a0c 100%)}

/* process */
.step{position:absolute;width:320px}
.step-badge{position:absolute;left:0;top:0;width:80px;height:80px;border-radius:50%;background:var(--ink)}
.step-badge span{position:absolute;left:10px;top:7px;width:66px;height:66px;border-radius:50%;background:var(--orange);border:3px solid #fff;color:#fff;font-size:27px;font-weight:500;display:flex;align-items:center;justify-content:center}
.step h3{position:absolute;left:93px;top:-5px;font-size:12.5px;font-weight:700;color:var(--ink);white-space:nowrap}
.step p{position:absolute;left:93px;top:15px;width:194px;font-size:10.8px;line-height:15px;color:var(--muted)}

/* why */
.why-sub{position:absolute;left:0;width:100%;top:100px;text-align:center;font-size:12.5px;font-weight:700;color:var(--ink)}
.why-lead{position:absolute;left:304px;top:119px;width:414px;text-align:center;font-size:12.5px;line-height:16.5px;color:var(--text)}
.why-col{position:absolute;width:200px}
.why-col h3{font-size:12.5px;font-weight:700;color:var(--ink);white-space:nowrap;margin-bottom:10px}
.why-col p{font-size:12.5px;line-height:16.5px;color:var(--text)}
.why-left{left:38px;top:219px;text-align:right}
.why-right{left:784px;top:232px}

/* charts */
.chart-card{position:absolute;top:104px;height:385px;background:var(--panel)}
.chart-card svg{position:absolute;left:0;top:0}
.chart-label{font-family:'Montserrat',sans-serif}

/* thank you */
.thanks-mark{position:absolute;left:242px;top:81px;width:176px;height:176px;border-radius:50%;background:var(--orange)}
.thanks-name{position:absolute;left:438px;top:112px;font-size:56px;font-weight:800;color:var(--ink);line-height:58px;letter-spacing:2px}
.contact{position:absolute;top:368px;width:300px;text-align:center}
.contact .icon{width:40px;height:40px;margin:0 auto 10px;border-radius:50%;background:var(--orange);display:flex;align-items:center;justify-content:center}
.contact .label{font-size:16px;color:var(--ink);line-height:22px}
.divider{position:absolute;top:367px;width:1px;height:111px;background:var(--rule)}
</style>
</head>
<body>

<!-- Cover -->
<section class="slide cover" style="top:70px">
  <div class="cover-photo" role="img" aria-label="Dark studio workspace photograph behind the title"></div>
  <div class="cover-frame"></div>
  <div class="cover-mark"></div>
  <div class="cover-name">LARKFIELD STUDIO</div>
</section>

<!-- About -->
<section class="slide" style="top:690px">
  <div class="topline"></div>
  <div class="tab" style="width:173px">INTRODUCTION</div>
  <h1 class="about-title">ABOUT LARKFIELD STUDIO</h1>
  <p class="about-text">Sed ut perspiciatis unde omnis iste natus error sit voluptatem accusantium doloremque laudantium, totam rem aperiam, eaque ipsa quae ab illo inventore veritatis et quasi architecto beatae vitae dicta sunt explicabo. Nemo enim ipsam voluptatem quia voluptas sit aspernatur aut odit aut fugit, sed quia consequuntur magni dolores eos qui ratione voluptatem sequi nesciunt. Neque porro quisquam est, qui dolorem ipsum quia dolor sit amet, consectetur, adipisci velit, sed quia non numquam eius modi tempora incidunt ut labore et dolore magnam aliquam quaerat voluptatem. Ut enim ad minima veniam, quis nostrum exercitationem ullam corporis suscipit laboriosam, nisi ut aliquid ex ea commodi</p>
  <div class="about-photo" role="img" aria-label="Circular team photograph in warm orange tones"></div>
  <div class="footer-brand"><div class="dot"></div><div class="name">LARKFIELD STUDIO</div></div>
  <div class="page-no">02</div>
</section>

<!-- Process -->
<section class="slide" style="top:1310px">
  <div class="topline"></div>
  <div class="tab" style="width:173px">OUR PROCESS</div>
  <h2 class="slide-title" style="top:80px">OUR PROCESS</h2>

  <div class="step" style="left:37px;top:145px"><div class="step-badge"><span>01</span></div><h3>EXCEPTEUR SINT OCCAE</h3><p>Sed ut perspiciatis unde omnis iste natus error sit voluptatem accusantium doloremque lantium, totam rem aperiam, eaque ipsa quae ab illo inveore veritatis et quasi architecto beatae vitae dicta sunt explicabo. Nemo enim ipsam voluptatem quia voluptas sit aspernatur aut odit aut fugit, sed quia consequuntur magni dolores</p></div>
  <div class="step" style="left:369px;top:145px"><div class="step-badge"><span>02</span></div><h3>EXCEPTEUR SINT OCCAE</h3><p>Sed ut perspiciatis unde omnis iste natus error sit voluptatem accusantium doloremque lantium, totam rem aperiam, eaque ipsa quae ab illo inveore veritatis et quasi architecto beatae vitae dicta sunt explicabo. Nemo enim ipsam voluptatem quia voluptas sit aspernatur aut odit aut fugit, sed quia consequuntur magni dolores</p></div>
  <div class="step" style="left:699px;top:140px"><div class="step-badge"><span>03</span></div><h3>EXCEPTEUR SINT OCCAE</h3><p>Sed ut perspiciatis unde omnis iste natus error sit voluptatem accusantium doloremque lantium, totam rem aperiam, eaque ipsa quae ab illo inveore veritatis et quasi architecto beatae vitae dicta sunt explicabo. Nemo enim ipsam voluptatem quia voluptas sit aspernatur aut odit aut fugit, sed quia consequuntur magni dolores</p></div>
  <div class="step" style="left:37px;top:358px"><div class="step-badge"><span>04</span></div><h3>EXCEPTEUR SINT OCCAE</h3><p>Sed ut perspiciatis unde omnis iste natus error sit voluptatem accusantium doloremque lantium, totam rem aperiam, eaque ipsa quae ab illo inveore veritatis et quasi architecto beatae vitae dicta sunt explicabo. Nemo enim ipsam voluptatem quia voluptas sit aspernatur aut odit aut fugit, sed quia consequuntur magni dolores</p></div>
  <div class="step" style="left:369px;top:358px"><div class="step-badge"><span>05</span></div><h3>EXCEPTEUR SINT OCCAE</h3><p>Sed ut perspiciatis unde omnis iste natus error sit voluptatem accusantium doloremque lantium, totam rem aperiam, eaque ipsa quae ab illo inveore veritatis et quasi architecto beatae vitae dicta sunt explicabo. Nemo enim ipsam voluptatem quia voluptas sit aspernatur aut odit aut fugit, sed quia consequuntur magni dolores</p></div>
  <div class="step" style="left:699px;top:353px"><div class="step-badge"><span>06</span></div><h3>EXCEPTEUR SINT OCCAE</h3><p>Sed ut perspiciatis unde omnis iste natus error sit voluptatem accusantium doloremque lantium, totam rem aperiam, eaque ipsa quae ab illo inveore veritatis et quasi architecto beatae vitae dicta sunt explicabo. Nemo enim ipsam voluptatem quia voluptas sit aspernatur aut odit aut fugit, sed quia consequuntur magni dolores</p></div>

  <div class="footer-brand"><div class="dot"></div><div class="name">LARKFIELD STUDIO</div></div>
  <div class="page-no">03</div>
</section>

<!-- Why choose us -->
<section class="slide" style="top:1930px">
  <div class="topline"></div>
  <div class="tab" style="width:195px">WHY CHOOSE US</div>
  <h2 class="slide-title" style="top:38px">WHY CHOOSE US</h2>
  <div class="why-sub">EXCEPTEUR SINT OCCAECAT</div>
  <p class="why-lead">Lorem ipsum dolor sit amet, consectetur adipiscing elit, sed do eiusmod tempor incididunt ut labore et dolore magna aliqua. Quis ipsum suspendisse ultrices gravida. Risus commodo viverra maecenas accumsan lacus vel facilisis.</p>

  <div class="why-col why-left"><h3>EXCEPTEUR SINT OCCAECAT</h3><p>Lorem ipsum dolor sit amet, consectetur adipiscing elit, sed do eiusmod tempor incididunt ut labore et dolore magna aliqua. Quis ipsum suspendisse ultrices gravida. Risus commodo viverra maecenas accumsan lacus vel facilisis.</p></div>
  <div class="why-col why-right"><h3>EXCEPTEUR SINT OCCAECAT</h3><p>Lorem ipsum dolor sit amet, consectetur adipiscing elit, sed do eiusmod tempor incididunt ut labore et dolore magna aliqua. Quis ipsum suspendisse ultrices gravida. Risus commodo viverra maecenas accumsan lacus vel facilisis.</p></div>

  <svg class="abs" style="left:0;top:0" width="1022" height="575" viewBox="0 0 1022 575">
    <circle cx="511" cy="500" r="255" fill="none" stroke="var(--orange)" stroke-width="1.5" stroke-dasharray="5 5"/>
    <circle cx="516" cy="683" r="145" fill="var(--orange)"/>
    <g>
      <circle cx="517" cy="241" r="31" fill="#fff" stroke="var(--orange)" stroke-width="5" stroke-dasharray="100 95" transform="rotate(30 517 241)"/>
      <path d="M503 236 h6 l12 -8 v24 l-12 -8 h-6 z" fill="none" stroke="var(--ink)" stroke-width="1.6"/>
      <circle cx="528" cy="248" r="6" fill="none" stroke="var(--ink)" stroke-width="1.6"/>
      <text x="528" y="251" font-size="8" text-anchor="middle" fill="var(--ink)" font-family="Montserrat,sans-serif" font-weight="700">$</text>
    </g>
    <g>
      <circle cx="293" cy="360" r="31" fill="#fff" stroke="var(--orange)" stroke-width="5" stroke-dasharray="100 95" transform="rotate(-40 293 360)"/>
      <rect x="282" y="346" width="15" height="26" rx="2" fill="none" stroke="var(--ink)" stroke-width="1.6"/>
      <path d="M296 356 l8 -5 v16 l-8 -5 z" fill="none" stroke="var(--orange)" stroke-width="1.6"/>
    </g>
    <g>
      <circle cx="734" cy="360" r="31" fill="#fff" stroke="var(--orange)" stroke-width="5" stroke-dasharray="100 95" transform="rotate(100 734 360)"/>
      <rect x="720" y="348" width="22" height="16" fill="none" stroke="var(--ink)" stroke-width="1.6"/>
      <path d="M723 360 l5 -5 l4 3 l6 -6" fill="none" stroke="var(--orange)" stroke-width="1.6"/>
      <line x1="718" y1="368" x2="744" y2="368" stroke="var(--ink)" stroke-width="1.6"/>
      <circle cx="746" cy="348" r="5" fill="none" stroke="var(--ink)" stroke-width="1.6"/>
    </g>
  </svg>

  <div class="footer-brand"><div class="dot"></div><div class="name">LARKFIELD STUDIO</div></div>
  <div class="page-no">04</div>
</section>

<!-- Advertising chart -->
<section class="slide grey" style="top:2549px">
  <div class="topline"></div>
  <div class="tab" style="width:200px">ADVERTISING CHART</div>
  <h2 class="slide-title" style="top:40px">ADVERTISING CHART</h2>

  <div class="chart-card" style="left:40px;width:507px">
    <svg width="507" height="385" viewBox="0 0 507 385" class="chart-label">
      <text x="19" y="28" font-size="12" font-weight="500" fill="var(--ink)">ANALYTICS</text>
      <rect x="348" y="38" width="56" height="18" rx="2" fill="none" stroke="#e2e2e2"/>
      <circle cx="357" cy="47" r="3" fill="var(--orange)"/><text x="364" y="50" font-size="8" fill="#888">Users</text>
      <rect x="410" y="38" width="72" height="18" rx="2" fill="none" stroke="#e2e2e2"/>
      <circle cx="419" cy="47" r="3" fill="var(--ink)"/><text x="426" y="50" font-size="8" fill="#888">Customers</text>
      <g font-size="10" fill="#888" text-anchor="middle">
        <text x="36" y="107">800</text><text x="36" y="135">700</text><text x="36" y="164">600</text><text x="36" y="192">500</text><text x="36" y="221">400</text><text x="36" y="249">300</text><text x="36" y="278">200</text><text x="36" y="306">100</text>
      </g>
      <g>
        <rect x="74" y="164" width="24" height="71" fill="var(--orange)"/><rect x="74" y="235" width="24" height="97" fill="var(--ink)"/>
        <rect x="109" y="278" width="24" height="26" fill="var(--orange)"/><rect x="109" y="304" width="24" height="28" fill="var(--ink)"/>
        <rect x="144" y="272" width="24" height="32" fill="var(--orange)"/><rect x="144" y="304" width="24" height="28" fill="var(--ink)"/>
        <rect x="179" y="266" width="24" height="38" fill="var(--orange)"/><rect x="179" y="304" width="24" height="28" fill="var(--ink)"/>
        <rect x="213" y="184" width="24" height="51" fill="var(--orange)"/><rect x="213" y="235" width="24" height="97" fill="var(--ink)"/>
        <rect x="248" y="224" width="24" height="35" fill="var(--orange)"/><rect x="248" y="259" width="24" height="73" fill="var(--ink)"/>
        <rect x="283" y="136" width="24" height="99" fill="var(--orange)"/><rect x="283" y="235" width="24" height="97" fill="var(--ink)"/>
        <rect x="318" y="181" width="24" height="54" fill="var(--orange)"/><rect x="318" y="235" width="24" height="97" fill="var(--ink)"/>
        <rect x="353" y="172" width="24" height="63" fill="var(--orange)"/><rect x="353" y="235" width="24" height="97" fill="var(--ink)"/>
        <rect x="387" y="218" width="24" height="41" fill="var(--orange)"/><rect x="387" y="259" width="24" height="73" fill="var(--ink)"/>
        <rect x="422" y="184" width="24" height="51" fill="var(--orange)"/><rect x="422" y="235" width="24" height="97" fill="var(--ink)"/>
        <rect x="457" y="178" width="24" height="57" fill="var(--orange)"/><rect x="457" y="235" width="24" height="97" fill="var(--ink)"/>
      </g>
      <g font-size="10" fill="#888" text-anchor="middle">
        <text x="86" y="340">Jan</text><text x="121" y="340">Feb</text><text x="156" y="340">Mar</text><text x="191" y="340">Apr</text><text x="225" y="340">May</text><text x="260" y="340">Jun</text><text x="295" y="340">Jul</text><text x="330" y="340">Aug</text><text x="365" y="340">Sep</text><text x="399" y="340">Oct</text><text x="434" y="340">Nov</text><text x="469" y="340">Dec</text>
      </g>
    </svg>
  </div>

  <div class="chart-card" style="left:573px;width:414px">
    <svg width="414" height="385" viewBox="0 0 414 385" class="chart-label">
      <text x="15" y="28" font-size="12" font-weight="500" fill="var(--ink)">STATISTIC</text>
      <rect x="257" y="38" width="56" height="18" rx="2" fill="none" stroke="#e2e2e2"/>
      <circle cx="266" cy="47" r="3" fill="var(--ink)"/><text x="273" y="50" font-size="8" fill="#888">Users</text>
      <rect x="319" y="38" width="72" height="18" rx="2" fill="none" stroke="#e2e2e2"/>
      <circle cx="328" cy="47" r="3" fill="var(--ink)"/><text x="335" y="50" font-size="8" fill="#888">Customers</text>
      <g stroke="#ececec" stroke-width="1">
        <line x1="50" y1="104" x2="395" y2="104"/><line x1="50" y1="132" x2="395" y2="132"/><line x1="50" y1="161" x2="395" y2="161"/><line x1="50" y1="189" x2="395" y2="189"/><line x1="50" y1="218" x2="395" y2="218"/><line x1="50" y1="246" x2="395" y2="246"/><line x1="50" y1="275" x2="395" y2="275"/><line x1="50" y1="303" x2="395" y2="303"/>
      </g>
      <g font-size="10" fill="#888" text-anchor="middle">
        <text x="30" y="107">800</text><text x="30" y="135">700</text><text x="30" y="164">600</text><text x="30" y="192">500</text><text x="30" y="221">400</text><text x="30" y="249">300</text><text x="30" y="278">200</text><text x="30" y="306">100</text>
      </g>
      <path d="M56 226 C77 226 77 189 98 189 C135 189 135 255 173 255 C210 255 210 189 247 189 C284 189 284 255 321 255 C352 255 352 195 383 195" fill="none" stroke="var(--orange)" stroke-width="3"/>
      <path d="M68 198 C99 198 99 255 130 255 C165 255 165 192 200 192 C237 192 237 263 274 263 C313 263 313 189 352 189 C370 189 370 221 388 221" fill="none" stroke="var(--ink)" stroke-width="3"/>
      <g fill="#fff" stroke="var(--orange)" stroke-width="2">
        <circle cx="56" cy="226" r="5"/><circle cx="173" cy="255" r="5"/><circle cx="247" cy="189" r="5"/><circle cx="321" cy="255" r="5"/><circle cx="383" cy="195" r="5"/>
      </g>
      <g fill="#fff" stroke="var(--ink)" stroke-width="2">
        <circle cx="68" cy="198" r="5"/><circle cx="200" cy="192" r="5"/><circle cx="274" cy="263" r="5"/><circle cx="352" cy="189" r="5"/><circle cx="388" cy="221" r="5"/>
      </g>
      <g font-size="10" fill="#888" text-anchor="middle">
        <text x="67" y="340">Jan</text><text x="102" y="340">Feb</text><text x="137" y="340">Mar</text><text x="172" y="340">Apr</text><text x="206" y="340">May</text><text x="241" y="340">Jun</text><text x="276" y="340">Jul</text><text x="311" y="340">Aug</text><text x="346" y="340">Sep</text><text x="380" y="340">Oct</text>
      </g>
    </svg>
  </div>

  <div class="footer-brand"><div class="dot"></div><div class="name">LARKFIELD STUDIO</div></div>
  <div class="page-no">05</div>
</section>

<!-- Thank you -->
<section class="slide grey" style="top:3169px">
  <div class="topline"></div>
  <div class="tab" style="width:173px">THANK YOU</div>
  <div class="thanks-mark"></div>
  <div class="thanks-name">LARKFIELD<br>STUDIO</div>
  <h2 class="slide-title" style="top:278px">THANK YOU</h2>

  <div class="contact" style="left:62px">
    <div class="icon"><svg width="20" height="20" viewBox="0 0 20 20"><path d="M10 2 a6 6 0 0 1 6 6 c0 4.5 -6 10 -6 10 s-6 -5.5 -6 -10 a6 6 0 0 1 6 -6z" fill="#fff"/><circle cx="10" cy="8" r="2.3" fill="var(--orange)"/></svg></div>
    <div class="label">Larkfield Studio<br>520 enim ipsam voluptatem</div>
  </div>
  <div class="divider" style="left:395px"></div>
  <div class="contact" style="left:379px">
    <div class="icon"><svg width="20" height="20" viewBox="0 0 20 20"><path d="M5 2 l3 0 l1.5 4 l-2 1.5 c1 2.2 2.8 4 5 5 l1.5 -2 l4 1.5 l0 3 c0 1 -1 2 -2 2 C9 17 3 11 3 4 c0 -1 1 -2 2 -2z" fill="#fff"/></svg></div>
    <div class="label">Phone<br>+1 888 8888 8888</div>
  </div>
  <div class="divider" style="left:673px"></div>
  <div class="contact" style="left:696px">
    <div class="icon"><svg width="20" height="20" viewBox="0 0 20 20"><rect x="3" y="5" width="14" height="10" rx="1.5" fill="#fff"/><path d="M3.5 6 l6.5 5 l6.5 -5" fill="none" stroke="var(--orange)" stroke-width="1.5"/></svg></div>
    <div class="label">Email<br>info@larkfieldstudio.com</div>
  </div>

  <div class="footer-brand"><div class="dot"></div><div class="name">LARKFIELD STUDIO</div></div>
  <div class="page-no">06</div>
</section>

</body>
</html>
```